10-year customer thank you card

We want a greeting card that our sales reps can send to companies/customers who have been with our company for 10 or more years. We're a software company, our corporate color is blue but we also like green, orange, and purple. We'd like something rather minimal/simplistic for this card, perhaps building off our tree logo. We're really open to ideas for this one. You must use the template files that are uploaded. Copy included in 10 year thank you card file; the copy may change based on how it looks when laid out
Updates

I updated our brief. We'd prefer a sans serif font. I also uploaded a blank infographic image that includes more of our approved colors.

Industry/Entity Type

Software

Font styles to use
Sans Serif

```html
<!DOCTYPE html>
<html lang="en">
<head>
<meta charset="utf-8">
<title>Ten Years – Thank You Card</title>
<link rel="stylesheet" href="https://fonts.googleapis.com/css2?family=Lato:wght@400&family=Great+Vibes&family=Pinyon+Script&display=swap">
<style>
  :root {
    --bg: #f2f2f2;
    --paper: #ffffff;
    --orange: #f5921e;
    --orange-soft: #f9b968;
    --yellow-soft: #f7ec7a;
    --blue: #1a73c9;
    --blue-soft: #a9cdee;
    --ink: #1c1c1c;
    --shadow: rgba(0, 0, 0, 0.28);
  }
  * { margin: 0; padding: 0; box-sizing: border-box; }
  html, body { width: 1200px; height: 933px; overflow: hidden; }
  body { background: var(--bg); position: relative; }

  .card {
    position: absolute;
    top: 126px;
    width: 500px;
    height: 680px;
    background: var(--paper);
    box-shadow: 4px 8px 18px var(--shadow);
    overflow: hidden;
  }
  .card--front { left: 70px; }
  .card--inside { left: 630px; }

  .pattern-band { position: absolute; left: 0; width: 100%; opacity: 0.85; }
  .pattern-band--top {
    top: 0; height: 88px;
    background: linear-gradient(90deg, var(--yellow-soft), var(--orange-soft));
  }
  .pattern-band--bottom {
    bottom: 0; height: 112px;
    background: linear-gradient(90deg, var(--orange-soft), var(--yellow-soft));
  }

  /* back panel of the fold, printed upside down */
  .back-brand {
    position: absolute;
    top: 150px; left: 0; width: 100%;
    text-align: center;
    transform: rotate(180deg);
    font-family: "Lato", sans-serif;
    font-weight: 400;
    color: var(--ink);
  }
  .back-brand__name {
    display: flex; align-items: center; justify-content: center; gap: 10px;
    font-size: 28px; line-height: 1;
  }
  .back-brand__dot { width: 14px; height: 14px; border-radius: 50%; background: var(--blue); }
  .back-brand__url { font-size: 13px; margin-top: 8px; }

  .wave { position: absolute; left: 0; top: 0; width: 500px; height: 680px; }

  .headline {
    position: absolute;
    top: 346px; left: 0; width: 100%;
    text-align: center;
    font-family: "Great Vibes", cursive;
    font-weight: 400;
    font-size: 44px;
    line-height: 1;
    color: var(--paper);
  }
  .emblem {
    position: absolute;
    top: 440px; left: 188px;
    width: 124px; height: 124px;
    border-radius: 50%;
    background: radial-gradient(circle, var(--blue-soft) 0 48%, transparent 49%);
    border: 5px solid var(--orange);
  }
  .thanks {
    position: absolute;
    top: 582px; left: 0; width: 100%;
    text-align: center;
    font-family: "Great Vibes", cursive;
    font-size: 30px;
    line-height: 1;
    color: var(--blue);
  }
  .bottom-band {
    position: absolute;
    left: 0; bottom: 0; width: 100%; height: 52px;
    background: var(--orange);
  }

  .message {
    position: absolute;
    top: 330px; left: 0; width: 100%;
    text-align: center;
    font-family: "Pinyon Script", cursive;
    font-size: 23px;
    line-height: 1.55;
    color: var(--ink);
  }
  .message__close { margin-top: 22px; }
</style>
</head>
<body>
  <section class="card card--front">
    <div class="pattern-band pattern-band--top" role="img" aria-label="Decorative orange brush-stroke pattern band"></div>

    <div class="back-brand">
      <div class="back-brand__name"><span class="back-brand__dot"></span>Halvern Systems</div>
      <div class="back-brand__url">www.halvernsystems.com</div>
    </div>

    <svg class="wave" viewBox="0 0 500 680" aria-hidden="true">
      <path d="M0 340 Q250 310 500 340 L500 449 Q250 380 0 476 Z" fill="var(--orange)"/>
    </svg>

    <h1 class="headline">Ten Years</h1>
    <div class="emblem" role="img" aria-label="Circular emblem decoration"></div>
    <p class="thanks">Thank you</p>
    <div class="bottom-band"></div>
  </section>

  <section class="card card--inside">
    <div class="message">
      <p>Thank you for being<br>a 10-year<br>Halvern customer.</p>
      <p class="message__close">We appreciate your business!</p>
    </div>
    <div class="pattern-band pattern-band--bottom" role="img" aria-label="Decorative orange brush-stroke pattern band"></div>
  </section>
</body>
</html>
```